Criação de Papelaria (6 itens) para Lumiar & Castelo
A empresa queria:
" EMPRESA FAMILIAR PRODUTORA DE GRÃOS hA 34 ANOS NO MERCADO, PIONEIRA EM IRRIGAÇÃO TIPO PIVO CENTRAL. "

```html
<!DOCTYPE html>
<html lang="pt-BR">
<head>
<meta charset="UTF-8">
<title>Lumiar &amp; Castelo — Adesivo</title>
<link rel="stylesheet" href="https://fonts.googleapis.com/css2?family=Cormorant+Garamond:wght@500&family=Montserrat:wght@400;500&display=swap">
<style>
  :root {
    --page: #ececea;
    --sticker: #8b8279;
    --gold: #c9a461;
    --ink-light: #f6f3ee;
  }
  * { margin: 0; padding: 0; box-sizing: border-box; }
  html, body {
    width: 1200px;
    height: 1200px;
    overflow: hidden;
    background: var(--page);
  }
  .canvas {
    position: relative;
    width: 1200px;
    height: 1200px;
  }
  .sticker {
    position: absolute;
    left: 100px;
    top: 100px;
    width: 1000px;
    height: 1000px;
    border-radius: 50%;
    background: var(--sticker);
  }
  .sticker-ring {
    position: absolute;
    inset: 34px;
    border-radius: 50%;
    border: 10px solid var(--gold);
  }
  .brand {
    position: absolute;
    left: 190px;
    top: 330px;
    display: flex;
    align-items: center;
    gap: 40px;
  }
  .brand-dot {
    width: 110px;
    height: 110px;
    border-radius: 50%;
    background: var(--gold);
    flex: none;
  }
  .brand-name {
    font-family: "Cormorant Garamond", serif;
    font-weight: 500;
    font-size: 96px;
    line-height: 0.95;
    color: var(--ink-light);
  }
  .contact {
    position: absolute;
    left: 0;
    right: 0;
    top: 600px;
    text-align: center;
    font-family: "Montserrat", sans-serif;
    color: var(--ink-light);
  }
  .contact-phone {
    font-size: 40px;
    font-weight: 500;
    letter-spacing: 1px;
    margin-bottom: 14px;
  }
  .contact-line {
    font-size: 30px;
    font-weight: 400;
    line-height: 1.4;
  }
</style>
</head>
<body>
  <main class="canvas">
    <section class="sticker">
      <div class="sticker-ring"></div>
      <div class="brand">
        <span class="brand-dot"></span>
        <h1 class="brand-name">Lumiar &amp;<br>Castelo</h1>
      </div>
      <address class="contact">
        <p class="contact-phone">(00) 0000-0000</p>
        <p class="contact-line">contato@lumiarcastelo.com.br</p>
        <p class="contact-line">Rua exemplo, 000 Cidade - UF</p>
        <p class="contact-line">CEP: 00000-000</p>
      </address>
    </section>
  </main>
</body>
</html>
```